Business Card Design for Mabel's Larder

We make food for dogs.
Business Card Design (using the logo designed by you). Our Brand color is a bright canary yellow. For example our signage is predominantly yellow, with the logo in black. I'd like the card also to use that imagery.
Feel free to use the two sides creatively.
Vertical Design is also great.

Industry/Entity Type

Pet food

Contact Information for Business Card

Name, email, website, phone no

Font styles to use
Sans Serif

Colors
59FF00
82FF00
B8FF75
E3FFCB
F4FFEA
FFF300
FFF600
FEFA6F
FFFEC7
FFFEE8

Requirements
Nice to have
• A graphic in the same brush stroke style of the logo shoeing a doggy bowl of food

```html
<!DOCTYPE html>
<html lang="en">
<head>
<meta charset="utf-8">
<title>Mabel's Larder — Business Card</title>
<link href="https://fonts.googleapis.com/css2?family=Arimo:wght@400;700&display=swap" rel="stylesheet">
<style>
  :root {
    --canary: #ffe14a;
    --card: #1b1c1e;
    --band: #2c2d2f;
    --ink: #ffffff;
    --backdrop: #2a2a2b;
  }
  * { box-sizing: border-box; margin: 0; padding: 0; }
  html, body { width: 1200px; height: 1107px; overflow: hidden; }
  body {
    background: var(--backdrop);
    font-family: "Arimo", Arial, sans-serif;
    display: flex;
    align-items: center;
    justify-content: center;
    gap: 80px;
  }
  .card {
    position: relative;
    width: 420px;
    height: 700px;
    background: var(--card);
    border: 10px solid var(--canary);
    box-shadow: 0 18px 40px rgba(0,0,0,.45);
  }
  .brand-name {
    position: absolute;
    left: 0; right: 0;
    text-align: center;
    color: var(--canary);
    font-weight: 700;
    font-size: 40px;
    letter-spacing: 1px;
    text-transform: uppercase;
  }
  .card-front .brand-name { top: 190px; }
  .card-back .brand-name { top: 300px; }

  .name-band {
    position: absolute;
    left: 0; right: 0;
    top: 330px;
    height: 96px;
    background: var(--band);
    padding: 20px 0 0 40px;
  }
  .name-band::before,
  .name-band::after {
    content: "";
    position: absolute;
    width: 10px;
    height: 48px;
    background: var(--canary);
  }
  .name-band::before { left: 0; top: 0; }
  .name-band::after { right: 0; bottom: 0; }
  .person-name {
    color: var(--canary);
    font-size: 28px;
    letter-spacing: 1px;
    line-height: 1;
  }
  .person-name .first { font-weight: 700; }
  .person-name .last { font-weight: 400; }
  .person-role {
    color: var(--ink);
    font-size: 19px;
    margin-top: 6px;
  }

  .address {
    position: absolute;
    left: 40px;
    top: 460px;
    color: var(--ink);
    font-size: 21px;
    line-height: 1.35;
  }
  .contact-list {
    position: absolute;
    left: 22px;
    top: 556px;
    list-style: none;
    color: var(--ink);
    font-size: 20px;
  }
  .contact-list li {
    display: flex;
    align-items: center;
    gap: 12px;
    height: 32px;
  }
  .contact-list svg { width: 20px; height: 20px; flex: none; }

  .back-site {
    position: absolute;
    left: 0; right: 0;
    bottom: 70px;
    text-align: center;
    color: var(--canary);
    font-size: 17px;
    letter-spacing: 5px;
  }
</style>
</head>
<body>
  <section class="card card-front">
    <div class="brand-name">Mabel's Larder</div>
    <div class="name-band">
      <div class="person-name"><span class="first">OWEN</span> <span class="last">HARTLEY</span></div>
      <div class="person-role">Manager</div>
    </div>
    <div class="address">Your Address, City<br>State, Zip 0000</div>
    <ul class="contact-list">
      <li>
        <svg viewBox="0 0 24 24" fill="var(--canary)"><path d="M6.6 10.8a15.1 15.1 0 0 0 6.6 6.6l2.2-2.2a1 1 0 0 1 1-.25 11.4 11.4 0 0 0 3.6.57 1 1 0 0 1 1 1V20a1 1 0 0 1-1 1A17 17 0 0 1 3 4a1 1 0 0 1 1-1h3.5a1 1 0 0 1 1 1c0 1.25.2 2.45.57 3.57a1 1 0 0 1-.25 1z"/></svg>
        <span>555-014-2277</span>
      </li>
      <li>
        <svg viewBox="0 0 24 24" fill="none" stroke="var(--canary)" stroke-width="2"><rect x="2" y="5" width="20" height="14"/><path d="M2 5l10 8 10-8"/></svg>
        <span>hello@mabelslarder.com</span>
      </li>
      <li>
        <svg viewBox="0 0 24 24" fill="none" stroke="var(--canary)" stroke-width="2"><circle cx="12" cy="12" r="10"/><path d="M2 12h20M12 2a15 15 0 0 1 0 20M12 2a15 15 0 0 0 0 20"/></svg>
        <span>www.mabelslarder.com</span>
      </li>
    </ul>
  </section>

  <section class="card card-back">
    <div class="brand-name">Mabel's Larder</div>
    <div class="back-site">www.mabelslarder.com</div>
  </section>
</body>
</html>
```